Pixagram Business Card For Comedian

Hi,

I'd like a 2-sided business card that kind mimics an Pixagram page. I've attached screenshots with the copy and language that should be written on there.

I'd like it to be way more stylized and a bit more creative than what I did on Powerpoint. I just did a mockup so that you can have an idea. I'd like it to be designed and you to take a bit of creative imagery so that it doesn't look so static and monochromatic.

PLEASE BE CREATIVE WITH THESE DESIGNS. I DON'T WANT IT TO LOOK EXACTLY LIKE THE ATTACHED IMAGE OR EXACTLY LIKE AN PIXAGRAM PAGE. I want to use it as inspiration to create something that looks more sleek, and creative. I don't want the colors to just be boring gray, and blue. Have fun and spice it up a bit!

Check out my website DanaWellmore.com to see the colors and fonts I use for my branding.

For the main photo: Here's a link with the hi-res photo: !https://www.filecrate.example/s/q8wtm3hzr5bdk2p/Dana-Wellmore-C71F2254.jpg?dl=0

For the thumbnail icon photo, you can use this: https://www.filecrate.example/s/vn4rx9kplw2tjdm/Dana%20Wellmore%20Glass%20Yard%20Headshot.jpg?dl=0

Use the Standard Business Card Template from Plinx.com:
https://help.plinx.example/hc/en-us/article_attachments/318274905/Standard_Size__US__Business_Cards_Portrait.jpg

Please let me know if you have any questions.
Updates

Industry/Entity Type

Business

Contact Information for Business Card

All of the text and copy has been provided on the attached jpg.

Colors
33a6d7
0255a3
aaaaaa
dbdbdb
1b1b1b

Requirements
Should not have
• A Hyperlink for the Email Addresses

```html
<!DOCTYPE html>
<html lang="en">
<head>
<meta charset="utf-8">
<title>Dana Wellmore Business Card</title>
<link href="https://fonts.googleapis.com/css2?family=Roboto+Condensed:wght@400;500&family=Source+Sans+3:ital,wght@0,400;1,400&family=Montserrat:wght@700&display=swap" rel="stylesheet">
<style>
  :root {
    --brand-blue: #33a6d7;
    --ink: #1b1b1b;
    --black: #0d0d0d;
    --white: #ffffff;
    --light-grey: #dbdbdb;
    --mid-grey: #aaaaaa;
    --backdrop: #b9b9bc;
  }
  * { box-sizing: border-box; margin: 0; padding: 0; }
  html, body { width: 1146px; height: 1200px; overflow: hidden; }
  body {
    background: var(--backdrop);
    font-family: "Source Sans 3", "Helvetica Neue", Arial, sans-serif;
    color: var(--ink);
    position: relative;
  }
  .card { position: absolute; box-shadow: 0 10px 24px rgba(0,0,0,.25); }

  /* Front (portrait) */
  .card-front { left: 60px; top: 160px; width: 500px; height: 875px; background: var(--white); }
  .front-header {
    height: 90px; background: var(--black);
    display: flex; align-items: center; justify-content: center;
  }
  .wordmark {
    font-family: "Roboto Condensed", "Arial Narrow", sans-serif;
    font-weight: 500; color: var(--brand-blue); font-size: 34px; letter-spacing: .5px;
  }
  .hero-photo {
    position: relative; height: 250px;
    background: linear-gradient(110deg, #d98aa8 0%, #3a2a26 25%, #1a1412 50%, #4a2e22 75%, #7fc3d8 100%);
  }
  .hero-roles {
    position: absolute; top: 30px; left: 0; right: 0;
    display: flex; justify-content: space-around; padding: 0 40px;
    font-family: "Roboto Condensed", "Arial Narrow", sans-serif;
    color: var(--light-grey); font-size: 31px; letter-spacing: 1px;
  }
  .front-body { position: relative; height: 322px; }
  .front-block { position: absolute; left: 49px; right: 24px; }
  .booking { top: 27px; }
  .about { top: 128px; }
  .seen-on { top: 246px; }
  .section-label {
    font-family: "Roboto Condensed", "Arial Narrow", sans-serif;
    font-weight: 400;
    color: var(--brand-blue); font-size: 23px; letter-spacing: 1px; line-height: 1;
  }
  .booking .section-label { margin-bottom: 2px; }
  .booking-email { font-style: italic; font-size: 21px; line-height: 28px; }
  .about .section-label { margin-bottom: 4px; }
  .about p { font-size: 18.5px; line-height: 23px; }
  .seen-on { font-size: 18.5px; line-height: 23px; }
  .seen-on .section-label { display: inline; margin-right: 3px; }
  .url-band {
    height: 50px; background: var(--black); color: var(--white);
    display: flex; align-items: center; justify-content: center;
    font-family: "Roboto Condensed", "Arial Narrow", sans-serif; font-size: 35px; letter-spacing: .5px;
  }
  .social { padding-top: 22px; text-align: center; }
  .social-title {
    display: flex; align-items: center; justify-content: center; gap: 10px;
    font-family: "Montserrat", Arial, sans-serif; font-weight: 700;
    color: var(--brand-blue); font-size: 15px; letter-spacing: 4px;
  }
  .social-title::before, .social-title::after {
    content: ""; width: 28px; height: 2px; background: var(--brand-blue);
  }
  .social-list { display: flex; justify-content: center; gap: 8px; margin-top: 14px; list-style: none; }
  .social-item { width: 100px; display: flex; flex-direction: column; align-items: center; }
  .social-dot { width: 44px; height: 44px; border-radius: 50%; background: var(--brand-blue); }
  .social-network { color: var(--brand-blue); font-size: 12px; line-height: 15px; margin-top: 2px; }
  .social-handle { font-size: 17px; line-height: 20px; }

  /* Back (landscape) */
  .card-back {
    left: 600px; top: 440px; width: 486px; height: 278px; background: var(--black);
    display: flex; flex-direction: column; align-items: center; justify-content: center;
  }
  .card-back .wordmark { font-size: 52px; }
  .back-roles {
    margin-top: 10px;
    font-family: "Roboto Condensed", "Arial Narrow", sans-serif;
    color: var(--light-grey); font-size: 24px; letter-spacing: 1px;
  }
  .back-roles .divider { color: var(--brand-blue); margin: 0 6px; }
</style>
</head>
<body>
  <section class="card card-front">
    <header class="front-header"><span class="wordmark">Dana Wellmore</span></header>
    <div class="hero-photo" role="img" aria-label="Photo of the comedian holding hands over her face wearing Glass Yard rings">
      <div class="hero-roles"><span>COMEDIAN</span><span>ACTRESS</span><span>WRITER</span></div>
    </div>
    <div class="front-body">
      <div class="front-block booking">
        <h2 class="section-label">FOR BOOKING</h2>
        <p class="booking-email">Tessa@BrightfieldTalent.com</p>
        <p class="booking-email">Mara.Holloway@quillagency.com</p>
      </div>
      <div class="front-block about">
        <h2 class="section-label">ABOUT</h2>
        <p>Stand Up Comedian. I Host. I Write. I Act.<br>I Dance. I Do Not Sing Unless I’m In The Shower.<br>I Accept Tips. (Not On Jokes, But On Cashly).</p>
      </div>
      <p class="front-block seen-on"><span class="section-label">AS SEEN ON:</span>Northwave, Laugh Channel,<br>Pulse TV, Real Tv, Edge And Vibe.</p>
    </div>
    <div class="url-band">WWW.DANAWELLMORE.COM</div>
    <div class="social">
      <p class="social-title">LET’S BE FRIENDS</p>
      <ul class="social-list">
        <li class="social-item"><span class="social-dot"></span><span class="social-network">Friendly</span><span class="social-handle">/danawellmore</span></li>
        <li class="social-item"><span class="social-dot"></span><span class="social-network">Chirper</span><span class="social-handle">/overglam</span></li>
        <li class="social-item"><span class="social-dot"></span><span class="social-network">Pixagram</span><span class="social-handle">/overglam</span></li>
      </ul>
    </div>
  </section>

  <section class="card card-back">
    <span class="wordmark">Dana Wellmore</span>
    <p class="back-roles">COMEDIAN<span class="divider">|</span>ACTRESS<span class="divider">|</span>WRITER</p>
  </section>
</body>
</html>
```